Velmora ICT is an ICT Project Services, ICT Architecture and Cloud consultation service business. I need a web site that is simple and looks professional and can grow with my business. I'll leave the creativity and colours up to you as the creative professionals.
Our ICT Project Services specialise in small to medium ICT Projects for government agencies and private organisations and Defence. Our project consultancy services helps our clients get to project execution, Projects as a Service. More information on the offering to be provided.
Cloud services consultation aide and manage in getting clients into the cloud, utilising our technical experience and project management.
I need additional tabs on the site to cater for my additional services.
I am about to offer Quorvane Cloud Certification which will be a paid monthly subscription.
I also require a tab that focuses on our developed Project software. Project as a service. Essentially a step by step application that controls and runs the project from execution to closure for small (complex service requests) projects under $100000.
Happy to provide much more information.
Target Market(s)
Small to medium business, government agencies
Industry/Entity Type
It Company
Contact Information for Business Card
Velmora ICT
Business Project Management and Architectural Services
Project Management as a Service.
Logo Text
Velmora ICT Consultative Business, Project Management and Architectural Services
2 page
Requirements
Must have
- Additional tabs for the additional products ICT Training and Project Management Applicaiton

```html
<!DOCTYPE html>
<html lang="en">
<head>
<meta charset="utf-8">
<title>Velmora ICT</title>
<link rel="stylesheet" href="https://fonts.googleapis.com/css2?family=Roboto:ital,wght@0,300;0,400;0,500;0,700;1,300&family=Open+Sans:wght@400;600;700&display=swap">
<style>
:root{
  --blue:#0b74c9;
  --sky:#5bc8e0;
  --sky-dark:#3fb3cd;
  --ink:#111111;
  --text:#555555;
  --muted:#a9a9a9;
  --white:#ffffff;
  --line:#d9d9d9;
}
*{box-sizing:border-box;margin:0;padding:0}
html,body{width:1200px;height:3147px;overflow:hidden}
body{font-family:"Open Sans",Arial,sans-serif;color:var(--text);background:var(--white);position:relative}
.abs{position:absolute}

/* header */
.topbar{height:92px;position:relative}
.brand{left:109px;top:22px;display:flex;align-items:center;gap:14px}
.brand-mark{width:40px;height:40px;background:var(--blue);border-radius:50%}
.brand-name{font-family:"Roboto",sans-serif;font-weight:500;font-size:34px;color:var(--blue);letter-spacing:.5px}
.contact-item{top:24px;display:flex;gap:14px;align-items:center}
.contact-icon{width:36px;height:36px;border:2px solid var(--blue);border-radius:50%;display:flex;align-items:center;justify-content:center}
.contact-label{font-size:12px;font-weight:700;color:var(--blue);line-height:1.2}
.contact-value{font-size:16px;color:#333;line-height:1.3}

.nav{top:92px;left:0;width:1200px;height:44px;background:var(--ink);display:flex;justify-content:space-between;padding:0 104px 0 130px;align-items:center}
.nav a{color:var(--white);text-decoration:none;font-family:"Roboto",sans-serif;font-weight:500;font-size:13.5px;letter-spacing:.3px}

/* hero */
.hero{top:136px;left:0;width:1200px;height:470px;background:var(--sky)}
.hero-floor{top:418px;left:0;width:1200px;height:52px;background:var(--sky-dark)}
.hero-title{left:100px;top:122px;width:480px;font-family:"Open Sans",sans-serif;font-weight:700;font-size:22.5px;line-height:43px;color:#155a73}
.btn-start{left:98px;top:264px;width:142px;height:38px;background:var(--white);color:#222;font-family:"Roboto",sans-serif;font-weight:500;font-size:16px;display:flex;align-items:center;justify-content:center}
.hero-art{left:556px;top:30px;width:524px;height:410px;border-radius:8px;background:linear-gradient(180deg,#7ad4e8 0%,#4fbdd6 100%)}
.hero-dots{left:98px;top:426px;display:flex;gap:10px}
.hero-dots span{width:34px;height:5px;background:var(--white)}
.hero-dots span:first-child{background:var(--blue)}

/* section titles */
.sec-title{left:0;width:1200px;text-align:center;font-family:"Roboto",sans-serif;font-weight:400;font-size:44px;color:var(--ink)}
.sec-title em{font-style:normal;color:var(--blue)}
.sec-rule{left:560px;width:80px;height:3px;background:var(--blue)}
.sec-sub{left:0;width:1200px;text-align:center;font-family:"Roboto",sans-serif;font-style:italic;font-weight:300;font-size:17.5px;color:var(--muted)}

.welcome-text{left:120px;top:788px;width:960px;text-align:center;font-size:14.5px;line-height:27px;color:#555}
.btn-dark{left:514px;top:936px;width:172px;height:44px;background:#2b2b2b;color:var(--white);font-family:"Roboto",sans-serif;font-size:18px;display:flex;align-items:center;justify-content:center}

/* services */
.svc-band{top:1154px;left:0;width:1200px;height:216px;background:var(--blue)}
.svc-card{top:1049px;width:235px}
.svc-img{width:235px;height:214px}
.svc-label{margin-top:12px;text-align:center;font-family:"Roboto",sans-serif;font-weight:500;font-size:21px;color:var(--white)}
.svc-dots{top:1340px;left:572px;display:flex;gap:10px}
.svc-dots span{width:7px;height:7px;border-radius:50%;background:var(--white)}

/* why choose */
.feat-title{font-family:"Roboto",sans-serif;font-weight:500;font-size:17.5px;color:var(--blue);line-height:1.3}
.feat-text{font-size:13.5px;line-height:22px;color:#444;margin-top:4px}
.feat-text b{color:var(--blue);font-weight:400}
.right-align{text-align:right}
.core-mark{left:450px;top:1690px;width:300px;height:200px;display:flex;align-items:center;justify-content:center;gap:16px}
.core-dot{width:34px;height:34px;border-radius:50%;background:var(--blue)}
.core-name{font-family:"Roboto",sans-serif;font-weight:500;font-size:38px;color:var(--blue)}

/* blogs and testimonials */
.blogs{top:1983px;left:0;width:600px;height:425px;background:var(--blue)}
.testi{top:1983px;left:600px;width:600px;height:425px;background:var(--ink)}
.panel-title{top:52px;font-family:"Roboto",sans-serif;font-weight:500;font-size:30px;color:var(--white)}
.panel-title em{font-style:normal}
.blogs .panel-title em{color:var(--ink)}
.testi .panel-title em{color:var(--blue)}
.panel-rule{top:112px;height:1px;background:rgba(255,255,255,.45)}
.arrows{top:56px;display:flex;gap:6px}
.arrows span{width:24px;height:24px;border:2px solid var(--white);border-radius:3px;display:flex;align-items:center;justify-content:center}
.post{left:98px;width:470px;display:flex;gap:24px}
.post-date{width:48px;flex:none;text-align:center}
.post-day{background:var(--ink);color:var(--white);font-family:"Roboto",sans-serif;font-weight:700;font-size:22px;height:32px;line-height:32px}
.post-mon{background:var(--white);color:var(--blue);font-size:11px;font-weight:700;height:18px;line-height:18px}
.post-title{font-family:"Open Sans",sans-serif;font-weight:700;font-size:16px;color:var(--white)}
.post-text{font-size:13px;line-height:21px;color:#e6f1fb;margin-top:4px}
.post-sep{left:98px;width:470px;height:1px;background:rgba(255,255,255,.3)}
.quote-photo{left:52px;top:164px;width:72px;height:72px;transform:rotate(45deg);border:3px solid var(--blue);background:linear-gradient(135deg,#cfd8e0,#8f9ea9)}
.quote-text{left:183px;top:130px;width:370px;font-size:13.5px;line-height:26px;color:#e0e0e0}
.quote-mark{color:#9a9a9a;font-family:"Roboto",sans-serif;font-weight:700;font-size:22px;line-height:0}
.quote-name{left:158px;top:316px;font-family:"Open Sans",sans-serif;font-weight:700;font-size:16px;color:var(--blue)}
.stars{left:168px;top:348px;display:flex;gap:4px}

/* clients */
.client-row{top:2635px;left:96px;display:flex;gap:12px}
.client{width:143px;height:76px;border:1px solid var(--line);display:flex;align-items:center;justify-content:center;gap:8px;font-family:"Roboto",sans-serif;font-weight:500;font-size:21px;color:#222}
.client i{width:14px;height:14px;background:#222;border-radius:50%;display:block}
.chev{top:2646px}

/* newsletter */
.news{top:2776px;left:0;width:1200px;height:73px;background:var(--blue)}
.news-title{left:98px;top:18px;display:flex;align-items:center;gap:14px;font-family:"Roboto",sans-serif;font-weight:700;font-size:28px;color:var(--white);letter-spacing:.3px}
.news-icon{width:36px;height:36px;border-radius:50%;background:var(--ink);display:flex;align-items:center;justify-content:center}
.news-input{left:540px;top:18px;width:457px;height:38px;background:var(--white);font-size:13px;color:#666;padding:11px 12px}
.news-btn{left:997px;top:18px;width:103px;height:38px;background:var(--ink);color:var(--white);font-family:"Roboto",sans-serif;font-weight:700;font-size:15px;display:flex;align-items:center;justify-content:center}

/* footer */
.footer{top:2849px;left:0;width:1200px;height:262px;background:var(--ink);color:var(--white)}
.foot-title{font-family:"Roboto",sans-serif;font-weight:700;font-size:15px;color:var(--white);padding-bottom:8px;border-bottom:1px solid #555;width:140px;top:36px}
.foot-list{list-style:none;top:80px;font-size:12.5px;line-height:20.6px;color:#eee}
.foot-list li::before{content:"› ";color:var(--white)}
.foot-contact{top:80px;left:340px;font-size:12.5px;line-height:17px}
.fc-row{display:flex;gap:10px;margin-bottom:12px}
.fc-row svg{flex:none;margin-top:2px}
.map{left:625px;top:78px;width:250px;height:154px;background:linear-gradient(135deg,#e8e6df,#cfd9d3)}
.social{top:80px;left:976px;font-size:13px;line-height:38px}
.social-row{display:flex;align-items:center;gap:12px}
.social-row i{width:18px;height:18px;background:var(--white);display:block}
.copy{top:3111px;left:0;width:1200px;height:36px;background:var(--blue);color:var(--white);font-size:12.5px;text-align:center;line-height:36px}
</style>
</head>
<body>

<header class="topbar">
  <div class="abs brand"><span class="brand-mark"></span><span class="brand-name">Velmora ICT</span></div>
  <div class="abs contact-item" style="left:706px">
    <span class="contact-icon"><svg width="18" height="18" viewBox="0 0 24 24"><path d="M6.6 10.8a15 15 0 0 0 6.6 6.6l2.2-2.2a1 1 0 0 1 1-.25 11.4 11.4 0 0 0 3.6.57 1 1 0 0 1 1 1V20a1 1 0 0 1-1 1A17 17 0 0 1 3 4a1 1 0 0 1 1-1h3.5a1 1 0 0 1 1 1c0 1.25.2 2.45.57 3.57a1 1 0 0 1-.25 1z" fill="#0b74c9"/></svg></span>
    <div><div class="contact-label">PHONE</div><div class="contact-value">(0400) 555 0182</div></div>
  </div>
  <div class="abs contact-item" style="left:912px">
    <span class="contact-icon"><svg width="18" height="14" viewBox="0 0 24 18"><rect x="1" y="1" width="22" height="16" rx="2" fill="none" stroke="#0b74c9" stroke-width="2"/><path d="M1 2l11 8 11-8" fill="none" stroke="#0b74c9" stroke-width="2"/></svg></span>
    <div><div class="contact-label">EMAIL</div><div class="contact-value">info@velmoraict.com</div></div>
  </div>
</header>

<nav class="abs nav">
  <a href="#">HOME</a><a href="#">ABOUT US</a><a href="#">SERVICES</a><a href="#">ICT TRAINING</a><a href="#">PROJECT MANAGEMENT APPLICATION</a><a href="#">CONTACT US</a>
</nav>

<section class="abs hero">
  <div class="abs hero-floor"></div>
  <h1 class="abs hero-title">We Provide A Full Range Of Consultancy Services And Support To Help Take The Hassles Out Of Your IT Projects.</h1>
  <a class="abs btn-start">Get Started</a>
  <div class="abs hero-art" role="img" aria-label="Illustration of three consultants at computer desks connected to a cloud"></div>
  <div class="abs hero-dots"><span></span><span></span><span></span></div>
</section>

<h2 class="abs sec-title" style="top:660px">WELCOME TO <em>VELMORA ICT</em></h2>
<div class="abs sec-rule" style="top:726px"></div>
<p class="abs sec-sub" style="top:742px">Lorem ipsum dolor sit amet consectetuer adipiscing elit Ut wisi enim ad minim veniam</p>
<p class="abs welcome-text">Lorem ipsum dolor sit amet, consectetuer adipiscing elit, sed diam nonummy nibh euismod tincidunt ut laoreet dolore magna aliquam erat volutpat. Ut wisi enim ad minim veniam, quis nostrud exerci tation ullamcorper suscipit lobortis nisl ut aliquip ex ea commodo consequat. Duis autem vel eum iriure dolor in hendrerit in vulputate velit esse molestie consequat, vel illum dolore eu feugiat nulla facilisis at vero eros et accumsan et iusto odio dignissim qui blandit praesent luptatum zzril delenit augue duis dolore te feugait nulla facilisi.</p>
<a class="abs btn-dark">Read More</a>

<section>
  <div class="abs svc-band"></div>
  <div class="abs svc-card" style="left:99px"><div class="svc-img" role="img" aria-label="Photo of a hand touching floating cloud icons" style="background:linear-gradient(135deg,#dbe9f5,#7fa9cf)"></div><div class="svc-label">Cloud Management</div></div>
  <div class="abs svc-card" style="left:355px"><div class="svc-img" role="img" aria-label="Illustration of cloud architecture network diagram" style="background:linear-gradient(135deg,#1f6fc7,#2e9be0)"></div><div class="svc-label">Cloud Architecture</div></div>
  <div class="abs svc-card" style="left:610px"><div class="svc-img" role="img" aria-label="Illustration of many connected clouds" style="background:linear-gradient(135deg,#3f6f95,#7fa3bd)"></div><div class="svc-label">MultiCloud Capability</div></div>
  <div class="abs svc-card" style="left:866px"><div class="svc-img" role="img" aria-label="Illustration of a ladder reaching a cloud on blue sky" style="background:linear-gradient(180deg,#1a8fe0,#8fd0f5)"></div><div class="svc-label">Cloud Migration</div></div>
  <div class="abs svc-dots"><span></span><span></span><span></span></div>
</section>

<h2 class="abs sec-title" style="top:1436px">WHY <em>CHOOSE US</em></h2>
<div class="abs sec-rule" style="top:1502px"></div>
<p class="abs sec-sub" style="top:1519px">Lorem ipsum dolor sit amet consectetuer adipiscing elit Ut wisi enim ad minim veniam</p>

<svg class="abs" style="left:0;top:1580px" width="1200" height="320" viewBox="0 0 1200 320">
  <g stroke="#0b74c9" stroke-width="2.5" fill="none">
    <line x1="464" y1="88" x2="520" y2="142"/>
    <line x1="388" y1="224" x2="470" y2="224"/>
    <line x1="746" y1="88" x2="690" y2="142"/>
    <line x1="820" y1="226" x2="740" y2="226"/>
  </g>
  <g fill="#fff" stroke="#555" stroke-width="2.5">
    <circle cx="432" cy="56" r="45"/><circle cx="778" cy="52" r="45"/>
    <circle cx="342" cy="224" r="45"/><circle cx="866" cy="226" r="45"/>
  </g>
  <g fill="none" stroke="#0b74c9" stroke-width="2.5" stroke-linecap="round">
    <circle cx="432" cy="42" r="6"/><circle cx="420" cy="62" r="5"/><circle cx="444" cy="62" r="5"/>
    <path d="M410 80a10 10 0 0 1 20 0M434 80a10 10 0 0 1 20 0"/>
    <path d="M760 52l12 12 24-24"/>
    <path d="M342 204l6 13 14 1-11 9 4 14-13-8-13 8 4-14-11-9 14-1z"/>
    <path d="M848 232v-8a18 18 0 0 1 36 0v8"/>
    <rect x="844" y="228" width="8" height="14" rx="2"/><rect x="880" y="228" width="8" height="14" rx="2"/>
  </g>
</svg>
<div class="abs core-mark"><span class="core-dot"></span><span class="core-name">Velmora ICT</span></div>

<div class="abs right-align" style="left:97px;top:1602px;width:270px">
  <div class="feat-title">Experienced &amp; Trained Staff</div>
  <div class="feat-text">Duis autem vel eum iriure<br><b>[+]</b>...hendrerit ulputat</div>
</div>
<div class="abs right-align" style="left:40px;top:1770px;width:235px">
  <div class="feat-title">Years of Experience</div>
  <div class="feat-text">Duis autem vel eum iriure<br><b>[+]</b>...hendrerit ulputat</div>
</div>
<div class="abs" style="left:846px;top:1602px;width:260px">
  <div class="feat-title">100 % Customer Satisfaction</div>
  <div class="feat-text">Duis autem vel eum iriure<br>hendrerit ulputat...<b>[+]</b></div>
</div>
<div class="abs" style="left:936px;top:1768px;width:200px">
  <div class="feat-title">24/7 Customer<br>Support Center</div>
  <div class="feat-text">Duis autem vel eum iriure<br>hendrerit ulputat...<b>[+]</b></div>
</div>

<section class="abs blogs">
  <h3 class="abs panel-title" style="left:98px">LETEST <em>BLOGS</em></h3>
  <div class="abs arrows" style="left:512px">
    <span><svg width="10" height="10" viewBox="0 0 10 10"><path d="M7 1L3 5l4 4" stroke="#fff" stroke-width="2" fill="none"/></svg></span>
    <span><svg width="10" height="10" viewBox="0 0 10 10"><path d="M3 1l4 4-4 4" stroke="#fff" stroke-width="2" fill="none"/></svg></span>
  </div>
  <div class="abs panel-rule" style="left:98px;width:436px"></div>
  <article class="abs post" style="top:142px">
    <div class="post-date"><div class="post-day">06</div><div class="post-mon">OCT</div></div>
    <div><div class="post-title">Diam Nonummy Nibh Euism Od Tincidunt</div><div class="post-text">Lorem ipsum dolor sit amet, consectetuer adipiscing elit, sedl diam nonummy nibh euism od tincidunt ut laoreet doloremoi magna aliquam erat volutpat.</div></div>
  </article>
  <div class="abs post-sep" style="top:246px"></div>
  <article class="abs post" style="top:270px">
    <div class="post-date"><div class="post-day">06</div><div class="post-mon">OCT</div></div>
    <div><div class="post-title">Diam Nonummy Nibh Euism Od Tincidunt</div><div class="post-text">Lorem ipsum dolor sit amet, consectetuer adipiscing elit, sedl diam nonummy nibh euism od tincidunt ut laoreet doloremoi magna aliquam erat volutpat.</div></div>
  </article>
</section>

<section class="abs testi">
  <h3 class="abs panel-title" style="left:30px">CLIENT <em>TESTIMONIALS</em></h3>
  <div class="abs arrows" style="left:442px">
    <span><svg width="10" height="10" viewBox="0 0 10 10"><path d="M7 1L3 5l4 4" stroke="#fff" stroke-width="2" fill="none"/></svg></span>
    <span style="border-color:#0b74c9"><svg width="10" height="10" viewBox="0 0 10 10"><path d="M3 1l4 4-4 4" stroke="#0b74c9" stroke-width="2" fill="none"/></svg></span>
  </div>
  <div class="abs panel-rule" style="left:30px;width:464px"></div>
  <div class="abs quote-photo" role="img" aria-label="Portrait photo of the client"></div>
  <p class="abs quote-text"><span class="quote-mark">“</span> Duis autem vel eum iriure dolor in hendrerit ink vulputate velit esse molestie consequat, vel illumkjm dolore eu feugiat nulla facilisis at vero eros etmolno accumsan et iusto odio dignissim qui blandit mormi vulputate velit esse molestie consequat, vel illumkm dolore eu feugiat nulla facilisis. <span class="quote-mark">”</span></p>
  <div class="abs quote-name">- Mr. Davin Orlake</div>
  <div class="abs stars">
    <svg width="86" height="16" viewBox="0 0 86 16">
      <path d="M8 1l2 5h5l-4 3 2 6-5-4-5 4 2-6-4-3h5z" fill="#fff"/>
      <path transform="translate(18 0)" d="M8 1l2 5h5l-4 3 2 6-5-4-5 4 2-6-4-3h5z" fill="#fff"/>
      <path transform="translate(36 0)" d="M8 1l2 5h5l-4 3 2 6-5-4-5 4 2-6-4-3h5z" fill="#fff"/>
      <path transform="translate(54 0)" d="M8 1l2 5h5l-4 3 2 6-5-4-5 4 2-6-4-3h5z" fill="#fff"/>
      <path transform="translate(72 0)" d="M8 1l2 5h5l-4 3 2 6-5-4-5 4 2-6-4-3h5z" fill="#0b74c9"/>
    </svg>
  </div>
</section>

<h2 class="abs sec-title" style="top:2470px">OUR <em>CLIENTS</em></h2>
<div class="abs sec-rule" style="top:2536px"></div>
<p class="abs sec-sub" style="top:2552px">Lorem ipsum dolor sit amet consectetuer adipiscing elit Ut wisi enim ad minim veniam</p>
<svg class="abs chev" style="left:50px" width="28" height="54" viewBox="0 0 28 54"><path d="M24 2L4 27l20 25" stroke="#ccc" stroke-width="2" fill="none"/></svg>
<svg class="abs chev" style="left:1118px" width="28" height="54" viewBox="0 0 28 54"><path d="M4 2l20 25-20 25" stroke="#ccc" stroke-width="2" fill="none"/></svg>
<div class="abs client-row">
  <div class="client"><i></i>BRIXEN</div>
  <div class="client">tallpoint</div>
  <div class="client"><i></i>Marlowe</div>
  <div class="client"><i></i>Quenta</div>
  <div class="client">Halvern</div>
  <div class="client"><i></i>BRIXEN</div>
</div>

<section class="abs news">
  <div class="abs news-title"><span class="news-icon"><svg width="18" height="13" viewBox="0 0 24 18"><rect x="1" y="1" width="22" height="16" rx="2" fill="#fff"/><path d="M1 2l11 8 11-8" fill="none" stroke="#111" stroke-width="2"/></svg></span>SUBSCRIBE NEWSLETTER</div>
  <div class="abs news-input">Enter you email and we'll stay in touch</div>
  <div class="abs news-btn">SUBSCRIBE</div>
</section>

<footer class="abs footer">
  <div class="abs foot-title" style="left:102px">QUICK LINKS</div>
  <ul class="abs foot-list" style="left:102px">
    <li>Home</li><li>About Us</li><li>Blog</li><li>Services</li><li>Solutions</li><li>Team</li><li>Contact Us</li>
  </ul>
  <div class="abs foot-title" style="left:338px;width:216px">CONTACT DETAILS</div>
  <div class="abs foot-contact">
    <div class="fc-row"><svg width="14" height="18" viewBox="0 0 14 18"><path d="M7 0a7 7 0 0 0-7 7c0 5 7 11 7 11s7-6 7-11a7 7 0 0 0-7-7z" fill="#0b74c9"/><circle cx="7" cy="7" r="2.5" fill="#111"/></svg><div><b>Velmora ICT</b><br>123, Lorem Ipsum Dolor Sit Amet,<br>Consectetuer Adipisci</div></div>
    <div class="fc-row"><svg width="14" height="14" viewBox="0 0 24 24"><path d="M6.6 10.8a15 15 0 0 0 6.6 6.6l2.2-2.2a1 1 0 0 1 1-.25 11.4 11.4 0 0 0 3.6.57 1 1 0 0 1 1 1V20a1 1 0 0 1-1 1A17 17 0 0 1 3 4a1 1 0 0 1 1-1h3.5a1 1 0 0 1 1 1c0 1.25.2 2.45.57 3.57a1 1 0 0 1-.25 1z" fill="#0b74c9"/></svg><b>0400.555.0182</b></div>
    <div class="fc-row"><svg width="14" height="14" viewBox="0 0 24 24"><path d="M6.6 10.8a15 15 0 0 0 6.6 6.6l2.2-2.2a1 1 0 0 1 1-.25 11.4 11.4 0 0 0 3.6.57 1 1 0 0 1 1 1V20a1 1 0 0 1-1 1A17 17 0 0 1 3 4a1 1 0 0 1 1-1h3.5a1 1 0 0 1 1 1c0 1.25.2 2.45.57 3.57a1 1 0 0 1-.25 1z" fill="#0b74c9"/></svg><b>0400.555.0196</b></div>
    <div class="fc-row"><svg width="14" height="11" viewBox="0 0 24 18"><rect x="1" y="1" width="22" height="16" rx="2" fill="none" stroke="#0b74c9" stroke-width="2"/><path d="M1 2l11 8 11-8" fill="none" stroke="#0b74c9" stroke-width="2"/></svg>info@velmoraict.com</div>
  </div>
  <div class="abs map" role="img" aria-label="Street map showing the office location"></div>
  <div class="abs foot-title" style="left:976px;width:124px">FOLLOW US</div>
  <div class="abs social">
    <div class="social-row"><i></i>Groupnest</div>
    <div class="social-row"><i></i>Shortpost</div>
    <div class="social-row"><i></i>Circlehub</div>
    <div class="social-row"><i></i>Workfolio</div>
  </div>
</footer>
<div class="abs copy">Copyright © 2016 Velmora ICT. All Rights Reserved.</div>

</body>
</html>
```